Anzeigengestaltung für Friseur- und Kosmetiksalon
Zielgruppe
750 Quadratmeter nur für die Schönheit - der Friseur- und Kosmetiksalon ``Studio Morgenrot`` in Sonnhalden besticht mit seinem ästhetischen Gesamtkonzept. Im Herzen Schwaigerns vereinen sich Hair Design, Kosmetik und Sport unter einem Dach. Neben dem topmodernen Interieur mit kostenlosen Parkmöglichkeiten und den besten Vermelune Paris Produkten überzeugt das großzügige Studio aber auch mit handwerklicher Qualität. Seit September 2017 dreht sich bei Friseurmeisterin Theresa Dinkelberg, ihrem Ehemann Bernd Dinkelberg und ihrem ausgebildeten Team alles rund um die Themen Beauty und Fitness.
Aufgabenstellung
Ich benötige zwei Anzeigen für Print.
Anzeige 1 = 90mm breit, 140mm hoch
Anzeige 2 = 90mm breit, 65mm hoch
Farbe: Graustufen
Im Anhang finden Beispiele und der Text soll übernommen werden.
Ich benötige die Anzeigen ohne Fotos von mir und meiner Kollegin.
Wobei bei der Anzeigengrösse 2 nicht alles umfänglich reinpassen wird. Dort halt die wichtigsten Infos.

```html
<!DOCTYPE html>
<html lang="de">
<head>
<meta charset="utf-8">
<title>Studio Morgenrot – Anzeige</title>
<link rel="stylesheet" href="https://fonts.googleapis.com/css2?family=Jost:wght@300;400;500;600;700&display=swap">
<style>
  :root {
    --backdrop: #e4e4e4;
    --paper: #ffffff;
    --ink: #2a2a2a;
    --ink-soft: #4a4a4a;
    --dark-band: #2e2e2e;
    --label-grey: #d6d6d6;
    --photo-light: #d9d9d9;
    --photo-mid: #8c8c8c;
    --photo-deep: #3a3a3a;
  }
  * { margin: 0; padding: 0; box-sizing: border-box; }
  html, body { width: 1200px; height: 1010px; overflow: hidden; }
  body {
    background: var(--backdrop);
    font-family: "Jost", "Futura", sans-serif;
    color: var(--ink);
  }
  .flyer {
    position: absolute;
    left: 260px; top: 25px;
    width: 680px; height: 960px;
    background: var(--paper);
    overflow: hidden;
    box-shadow: 0 6px 24px rgba(0,0,0,0.12);
  }
  .brand {
    position: absolute;
    left: 0; top: 40px; width: 680px;
    text-align: center;
  }
  .brand-owner {
    font-size: 13px; font-weight: 400; letter-spacing: 0.22em;
    color: var(--ink-soft);
  }
  .brand-name {
    font-size: 38px; font-weight: 400; letter-spacing: 0.06em;
    color: var(--ink); line-height: 1.2; margin-top: 4px;
  }
  .brand-fields {
    font-size: 12px; font-weight: 400; letter-spacing: 0.3em;
    color: var(--ink-soft); margin-top: 4px;
  }
  .hero-shape { position: absolute; left: 0; top: 0; }
  .labels { position: absolute; left: 62px; top: 238px; width: 320px; }
  .label {
    display: block; height: 32px; line-height: 32px;
    background: var(--paper);
    padding-left: 28px;
    font-size: 14px; font-weight: 600; letter-spacing: 0.16em;
    text-transform: uppercase; color: var(--ink);
    margin-bottom: 6px;
  }
  .label--sub {
    background: var(--label-grey);
    font-weight: 300; letter-spacing: 0.02em; text-transform: none;
    font-size: 15px; padding-left: 64px;
  }
  .headline {
    position: absolute; left: 58px; top: 512px;
    font-size: 32px; font-weight: 500; letter-spacing: 0.18em;
    color: var(--ink);
  }
  .services {
    position: absolute;
    font-size: 14.5px; font-weight: 300; line-height: 21px;
    color: var(--ink-soft);
  }
  .services h2 {
    font-size: 17px; font-weight: 600; letter-spacing: 0.14em;
    color: var(--ink); margin-bottom: 8px;
  }
  .services p + h2 { margin-top: 16px; }
  .services--left { left: 60px; top: 582px; width: 272px; }
  .services--right { left: 360px; top: 582px; width: 292px; }
  .website {
    position: absolute; right: 36px; top: 856px;
    font-size: 15px; font-weight: 600; color: var(--ink);
  }
  .footer {
    position: absolute; left: 0; bottom: 0; width: 680px; height: 72px;
    background: var(--dark-band); color: var(--paper);
    font-size: 14px; font-weight: 300; letter-spacing: 0.03em;
    display: flex; align-items: center; justify-content: center;
  }
</style>
</head>
<body>
  <main class="flyer">
    <header class="brand">
      <div class="brand-owner">THERESA DINKELBERG</div>
      <div class="brand-name">STUDIO MORGENROT</div>
      <div class="brand-fields">FRISEUR &nbsp; KOSMETIK &nbsp; SCHÖNHEIT</div>
    </header>

    <svg class="hero-shape" width="680" height="520" viewBox="0 0 680 520">
      <defs>
        <linearGradient id="salon-tone" x1="0" y1="0" x2="1" y2="1">
          <stop offset="0" stop-color="var(--photo-deep)"/>
          <stop offset="0.45" stop-color="var(--photo-light)"/>
          <stop offset="1" stop-color="var(--photo-mid)"/>
        </linearGradient>
      </defs>
      <polygon points="0,200 420,200 420,385 300,500 0,500" fill="var(--dark-band)"/>
      <rect x="170" y="150" width="510" height="235" fill="url(#salon-tone)" role="img" aria-label="Innenansicht des Salons mit Frisierplätzen und Empfangstheke"/>
    </svg>

    <div class="labels">
      <span class="label">Kreatives Styling</span>
      <span class="label">Hochwertige Produkte</span>
      <span class="label label--sub">von Vermelune Paris</span>
      <span class="label">Exklusives Ambiente</span>
    </div>

    <h1 class="headline">IHR SALON IN SONNHALDEN</h1>

    <section class="services services--left">
      <h2>FRISEUR</h2>
      <p>Haar- &amp; Kopfhautdiagnose / Spezifische Haar- &amp; Kopfhautpflege / Behandlungen gegen Schuppen &amp; Haarausfall / Haarschnitt / Haarfarbe &amp; Strähnentechniken / Haarverlängerung &amp; -verdichtung / Brautstyling</p>
      <h2>ÄSTHETIK</h2>
      <p>Aquafacial / Mesoporation / BB Glow / BB Lips / Micro Needling / Ionen Lifting /</p>
    </section>

    <section class="services services--right">
      <p>Ultraschall &amp; Cellulite Behandlung / PowderBrows / Aquarell Lips / Fachkosmetik / Gesichtspflege / Nagelmodellage / Zahnbleaching</p>
      <h2>KOSMETIK</h2>
      <p>Make-up / Wimpernverlängerung / Maniküre / Nagelmodellage / Fachfußpflege / Spezial&shy;behandlungen bei Akne, Falten, Pigmentstörungen / Dauerhafte Haarentfernung (IPL/SHR) / Microblading Augenbrauen / Lippen- &amp; Lidstrichpigmentierung</p>
    </section>

    <div class="website">www.studio-morgenrot.example</div>

    <footer class="footer">Lindenweg 12, 79999 Sonnhalden &nbsp;/&nbsp; +49 (0)1234 555012 &nbsp;/&nbsp; info@studio-morgenrot.example</footer>
  </main>
</body>
</html>
```